Package Design for 15 lines of Tea

I need design variations for 15 different Tea lines.
The tea will be packaged in Tin cylinders.
I have attached several pictures to show you an example of the display we are modelling after along with other references.
The 15 tea lines are:
Study Tea
Ingredients: Brazilian Mate, Mint
Energy Boost Tea
Ingredients: Yunnan Coffee, Dark Puer
Relaxation Tea
Ingredients: Lotus Flower, South African Rooibos
Beauty Tea
Ingredients: Rose, Chrysanthemum, Red Dates, Huangqi
Sore Throat Tea
Ingredients: Honeysuckle, Pang Da Hai, Chamomile, Licorice Root
Get Well Tea
Ingredients: Ginger, Rooibos, Orange peel, Chinese Angelica
Diet Tea
Ingredients: Puer, Hibiscus, Lemongrass, Lotus Plumule
Bedtime Tea
Ingredients: Apple, Orange, Chamomile
South African Rooibos Tea
(pure)
Brazilian Yerba Mate Tea
(pure)
Long Jing Green Tea
(pure)
Darjeeling Black Tea
(pure)
Nepal Golden Tea
(Pure)
Bai Mu Dan White Tea
(pure)
Phoenix Oolong Tea
(pure)
Every Tea Blend should have three unique symbols that describe the purpose and theme of the blend. (!!Please don't make specific reference to the ingredients of the blends because some of these ingredients may be changed later. Stick to focusing on the intended purpose of the tea blend!!)
I would like the symbols to keep the same brushlike style that is consistent with our company logo.
Please keep the three block structure. I suggest keeping to just one color per tea blend. This will help each blend stand out between one another. I have a sample of the "Diet Tea" attached that I did myself to give you an idea of the structure I'm looking for, but obviously it's just my amateur version. Hope you can make them look far more appealing.
The ultimate goal is to build a picture language unique to our brand. As more products are released, we intend to potentially have hundreds of symbols, each with it's own meaning. So it would be nice when you present your pictures if you explain its intended meaning or message.
Deminsions:
Cylinder type 1: 82mm*38mmH
circular labels (along with your design) will be placed on the cap of product, and then the cylinder will be slanted on it's side to display the cap towards the customer.
Cylinder type 2: 65mm*152mmH
the labels will be placed on the side of the cylinder. In this version, try lining the three symbols in a vertical position. If this looks awful to you then feel free to go back to the horizontal style, but it would be nice to see what the vertical version looks like for reference.
Updates
Due to the scope of this project, please take note that I just increased my budget an additional 500 dollars more.
I also just added a 100 dollar second place prize. Don't want to see hard work unrewarded.
Feel free to send a few samples and I will provide prompt feedback. Please don't feel that you must submit all 15 lines at the same time.
Project Deadline Extended
Reason: I am extending the deadline as I feel there are more detailed revisions that need to be made until final selection.
Target Market(s)
Middle to Upper Class Consumers in China
Industry/Entity Type
It Company
Other font styles liked:
- font similar to font on company logo
Requirements
Must have
- Tea Designs must be in harmony with company logo and theme.
Should not have
- Avoid using Chinese characters as symbols. They may seem cool to westerners, but it's tacky for Chinese consumers.

```html
<!DOCTYPE html>
<html lang="en">
<head>
<meta charset="utf-8">
<title>Ardenly – Blend Labels</title>
<link rel="stylesheet" href="https://fonts.googleapis.com/css2?family=Bebas+Neue&display=swap">
<style>
  :root {
    --page-bg: #eef0f2;
    --label-black: #0d0d0d;
    --panel-white: #f4f5f6;
    --brand-white: #f2f2f2;

    --study-ring: #1e9ad6;
    --study-title: #1a7fc1;
    --study-sub: #e8902a;

    --energy-ring: #d7201f;
    --energy-title: #b51a24;
    --energy-sub: #2a9ad6;

    --relax-ring: #a6c638;
    --relax-title: #a4c232;
    --relax-sub: #4aa7d9;
  }

  * { margin: 0; padding: 0; box-sizing: border-box; }

  html, body {
    width: 1200px;
    height: 650px;
    overflow: hidden;
    background: var(--page-bg);
  }

  .label-row {
    width: 1200px;
    height: 650px;
    display: flex;
    justify-content: space-around;
    align-items: center;
    padding: 0 40px;
  }

  .tea-label {
    position: relative;
    width: 330px;
    height: 330px;
    border-radius: 50%;
    border: 6px solid var(--ring);
    padding: 6px;
  }

  .tea-label__disc {
    width: 100%;
    height: 100%;
    border-radius: 50%;
    background: var(--label-black);
    display: flex;
    flex-direction: column;
    align-items: center;
    padding-top: 62px;
  }

  .brand-name {
    font-family: "Bebas Neue", "Arial Narrow", sans-serif;
    font-size: 32px;
    color: var(--brand-white);
    letter-spacing: 1.5px;
    line-height: 1;
    margin-bottom: 14px;
  }

  .blend-panel {
    width: 236px;
    background: var(--panel-white);
    text-align: center;
    padding: 8px 6px 6px;
  }

  .blend-title {
    font-family: "Bebas Neue", "Arial Narrow", sans-serif;
    font-size: 40px;
    line-height: 0.95;
    color: var(--title);
    white-space: nowrap;
  }

  .blend-title--long { font-size: 34px; line-height: 1.05; }

  .blend-ingredients {
    font-family: "Bebas Neue", "Arial Narrow", sans-serif;
    font-size: 17px;
    line-height: 1;
    color: var(--sub);
    letter-spacing: 0.4px;
    white-space: nowrap;
  }

  .blend-ingredients--small { font-size: 13px; padding: 2px 0; }

  .blend-symbol {
    margin-top: 16px;
    width: 54px;
    height: 76px;
    border-radius: 27px 27px 10px 10px;
    background: var(--ring);
  }

  .blend-symbol--bolt {
    width: 50px;
    border-radius: 6px;
  }

  .tea-label--study  { --ring: var(--study-ring);  --title: var(--study-title);  --sub: var(--study-sub); }
  .tea-label--energy { --ring: var(--energy-ring); --title: var(--energy-title); --sub: var(--energy-sub); }
  .tea-label--relax  { --ring: var(--relax-ring);  --title: var(--relax-title);  --sub: var(--relax-sub); }
</style>
</head>
<body>
  <main class="label-row">

    <section class="tea-label tea-label--study">
      <div class="tea-label__disc">
        <p class="brand-name">Ardenly</p>
        <div class="blend-panel">
          <h2 class="blend-title">Study Tea</h2>
          <p class="blend-ingredients">Brazilian Mate, Mint</p>
        </div>
        <div class="blend-symbol" role="img" aria-label="Brush-drawn light bulb symbol for focus"></div>
      </div>
    </section>

    <section class="tea-label tea-label--energy">
      <div class="tea-label__disc">
        <p class="brand-name">Ardenly</p>
        <div class="blend-panel">
          <h2 class="blend-title blend-title--long">Energy Boost Tea</h2>
          <p class="blend-ingredients">Yunnan Coffee, Dark Puer</p>
        </div>
        <div class="blend-symbol blend-symbol--bolt" role="img" aria-label="Brush-drawn lightning bolt symbol for energy"></div>
      </div>
    </section>

    <section class="tea-label tea-label--relax">
      <div class="tea-label__disc">
        <p class="brand-name">Ardenly</p>
        <div class="blend-panel">
          <h2 class="blend-title blend-title--long">Relaxation Tea</h2>
          <p class="blend-ingredients blend-ingredients--small">Lotus Flower, South African Rooibos</p>
        </div>
        <div class="blend-symbol" role="img" aria-label="Brush-drawn light bulb symbol for calm"></div>
      </div>
    </section>

  </main>
</body>
</html>
```